Etikett für Bierflaschen
Anforderungen:
Bitte entwerfen Sie Etiketten für Bierflaschen (Bügelflaschen), welches man ggf. auch als Logo für eine kleine Hausbrauerei benutzen kann.
Der Bezug zur Region sollte erkennbar sein. (Norddeutschland/Teufelsmoor).
Gut wäre, wenn eine Torfkahn-Zeichnung enthalten wäre.
Im Vorder-Etikett sollte der Name der Brauerei (Kranwieder Hausbrauerei), der Biername (58er) und der Biertyp (Bsp.Pilsener), haltbar bis,Vol% zu sehen sein.
Im hinteren Etikett (Flaschenrückseite) möchte ich das Bier beschreiben und die Inhaltsstoffe angeben. Evtl. könnten auch hier haltbar bis und/oder %vol. stehen. Last but not leased hat die Bügelflasche noch ein Etikett am Hals,
Unternehmensbeschreibung:
Hierbei handelt es sich um eine kleine Hausbrauerei, die noch nicht gegründet ist. Wichtig für den Vertrieb des Bieres ist der Bezug zur Region
Norddeutschland,Teufelsmoor,Torfkahn) Das Bier wird nicht in großen Mengen hergestellt. Vorgesehen sind kleinere Fässer und 1-Liter und 2-Literflaschen.
Zielgruppe:
Von jung bis alt.
Farben, Logo-Favoriten und weitere Anforderungen
Nur eine Idee:
Dunkel-Gelb am Rand (hier könnte der Name der Brauerei geschrieben sein), Der Torfkahn und die Landschaft braun.
Ansonsten hell z.B. grau
Die Bezeichnung des Biertyps könnte man je nach Biertyp in verschiedenen Farben hinterlegen.
Ein Beispiel einer anderen Brauerei (Mit Leuchtturm) ist als Datei beigefügt.
Hallo,
Mit freundlichen Grüßen
die Länge des Halsetiketts soll ca. 7,5cm sein. MfG

```html
<!DOCTYPE html>
<html lang="de">
<head>
<meta charset="utf-8">
<title>58er Pilsener – Etikettvarianten</title>
<link rel="stylesheet" href="https://fonts.googleapis.com/css2?family=Alegreya:wght@400;800&family=Alegreya+SC:wght@400;800&display=swap">
<style>
  :root {
    --page: #ffffff;
    --charcoal: #262626;
    --sage: #9bbca0;
    --cream: #f2f3e6;
    --stone: #e7e4dd;
    --slate: #5f5b5d;
    --mustard: #f2d33a;
    --rule-light: #b9b9b4;
  }
  html, body {
    margin: 0;
    padding: 0;
    width: 1130px;
    height: 1200px;
    overflow: hidden;
    background: var(--page);
  }
  .sheet {
    position: relative;
    width: 1130px;
    height: 1200px;
  }
  .label {
    position: absolute;
    width: 445px;
    height: 511px;
    border-radius: 14px;
    box-sizing: border-box;
    background: var(--bg);
    color: var(--ink);
  }
  .label--night  { left: 41px;  top: 41px;  --bg: var(--charcoal); --ink: var(--sage);     --boat: var(--sage);     --rule: var(--rule-light); }
  .label--moor   { left: 642px; top: 41px;  --bg: var(--sage);     --ink: var(--charcoal); --boat: var(--charcoal); --rule: var(--charcoal); }
  .label--linen  { left: 41px;  top: 651px; --bg: var(--cream);    --ink: var(--sage);     --boat: var(--sage);     --rule: var(--sage); }
  .label--heath  { left: 642px; top: 651px; --bg: var(--stone);    --ink: var(--slate);    --boat: var(--slate);    --rule: var(--mustard); border: 3px solid var(--mustard); }

  .boat-art {
    position: absolute;
    left: 160px;
    top: 68px;
    width: 126px;
    height: 160px;
    background: var(--boat);
    border-radius: 6px 30px 4px 4px;
  }
  .rule {
    position: absolute;
    left: 26px;
    width: 393px;
    height: 12px;
  }
  .rule--deck { top: 226px; }
  .rule--type { top: 429px; }
  .rule line { stroke: var(--rule); stroke-width: 2; }

  .beer-name {
    position: absolute;
    left: 0;
    right: 0;
    top: 262px;
    margin: 0;
    text-align: center;
    font-family: "Alegreya SC", Georgia, serif;
    font-weight: 800;
    font-size: 84px;
    line-height: 1;
    letter-spacing: 6px;
  }
  .brewery {
    position: absolute;
    left: 0;
    right: 0;
    top: 345px;
    margin: 0;
    text-align: center;
    font-family: "Alegreya", Georgia, serif;
    font-weight: 400;
    font-size: 27px;
    letter-spacing: 0.5px;
  }
  .label--moor .brewery,
  .label--linen .brewery,
  .label--heath .brewery {
    font-family: "Alegreya SC", Georgia, serif;
    font-size: 25px;
  }
  .beer-type {
    position: absolute;
    left: 0;
    right: 0;
    top: 420px;
    margin: 0;
    text-align: center;
    font-family: "Alegreya SC", Georgia, serif;
    font-weight: 800;
    font-size: 24px;
    line-height: 30px;
    letter-spacing: 2px;
  }
</style>
</head>
<body>
<main class="sheet">

  <section class="label label--night">
    <div class="boat-art" role="img" aria-label="Torfkahn mit Segel"></div>
    <svg class="rule rule--deck" viewBox="0 0 393 12"><line x1="0" y1="6" x2="393" y2="6"/><line x1="1" y1="0" x2="1" y2="12"/><line x1="392" y1="0" x2="392" y2="12"/></svg>
    <h1 class="beer-name">58ER</h1>
    <p class="brewery">Kranwieder Hausbrauerei</p>
    <svg class="rule rule--type" viewBox="0 0 393 12"><line x1="0" y1="6" x2="125" y2="6"/><line x1="268" y1="6" x2="393" y2="6"/><line x1="1" y1="0" x2="1" y2="12"/><line x1="392" y1="0" x2="392" y2="12"/></svg>
    <p class="beer-type">PILSENER</p>
  </section>

  <section class="label label--moor">
    <div class="boat-art" role="img" aria-label="Torfkahn mit Segel"></div>
    <svg class="rule rule--deck" viewBox="0 0 393 12"><line x1="0" y1="6" x2="393" y2="6"/><line x1="1" y1="0" x2="1" y2="12"/><line x1="392" y1="0" x2="392" y2="12"/></svg>
    <h1 class="beer-name">58ER</h1>
    <p class="brewery">KRANWIEDER HAUSBRAUEREI</p>
    <svg class="rule rule--type" viewBox="0 0 393 12"><line x1="0" y1="6" x2="125" y2="6"/><line x1="268" y1="6" x2="393" y2="6"/><line x1="1" y1="0" x2="1" y2="12"/><line x1="392" y1="0" x2="392" y2="12"/></svg>
    <p class="beer-type">PILSENER</p>
  </section>

  <section class="label label--linen">
    <div class="boat-art" role="img" aria-label="Torfkahn mit Segel"></div>
    <svg class="rule rule--deck" viewBox="0 0 393 12"><line x1="0" y1="6" x2="393" y2="6"/><line x1="1" y1="0" x2="1" y2="12"/><line x1="392" y1="0" x2="392" y2="12"/></svg>
    <h1 class="beer-name">58ER</h1>
    <p class="brewery">KRANWIEDER HAUSBRAUEREI</p>
    <svg class="rule rule--type" viewBox="0 0 393 12"><line x1="0" y1="6" x2="125" y2="6"/><line x1="268" y1="6" x2="393" y2="6"/><line x1="1" y1="0" x2="1" y2="12"/><line x1="392" y1="0" x2="392" y2="12"/></svg>
    <p class="beer-type">PILSENER</p>
  </section>

  <section class="label label--heath">
    <div class="boat-art" role="img" aria-label="Torfkahn mit Segel"></div>
    <svg class="rule rule--deck" viewBox="0 0 393 12"><line x1="0" y1="6" x2="393" y2="6"/><line x1="1" y1="0" x2="1" y2="12"/><line x1="392" y1="0" x2="392" y2="12"/></svg>
    <h1 class="beer-name">58ER</h1>
    <p class="brewery">KRANWIEDER HAUSBRAUEREI</p>
    <svg class="rule rule--type" viewBox="0 0 393 12"><line x1="0" y1="6" x2="125" y2="6"/><line x1="268" y1="6" x2="393" y2="6"/><line x1="1" y1="0" x2="1" y2="12"/><line x1="392" y1="0" x2="392" y2="12"/></svg>
    <p class="beer-type">PILSENER</p>
  </section>

</main>
</body>
</html>
```